Powerpoint presentation about personal finance

Investing 4$ per day is what has been required to become a millionaire by investing in the stock market from 1965 to 2015. Yet only 1% of the population is millionaire. This presentation is about the most common causes why people do not build significant wealth through their life. We intend to educate people with this presentation, but also build trust so they become client of our wealth management firm. Feel free to send us any question about this project.
Updates

Reason: I have uploaded the logo source file and an updated PPT file. Thanks

Target Market(s)

People with a willingness to save money between the age of 20 to 50 years old

Industry/Entity Type

Finance

Font styles to use
Sans Serif

Requirements
Must have
• We are looking at uniforming the design throughout the presentation with nice, classic tone colors, large font size as it needs to be visible 3 meters apart. The content of the presentation will be updated regularly.
Should not have
• cartoon style, not serious

```html
<!DOCTYPE html>
<html lang="fr">
<head>
<meta charset="utf-8">
<title>Présentation – Norvale</title>
<link rel="stylesheet" href="https://fonts.googleapis.com/css2?family=Fira+Sans:wght@400;500;600;700&display=swap">
<style>
  :root {
    --backdrop: #cbcbcb;
    --slide: #ffffff;
    --blue: #1a48a0;
    --green: #2e8b3c;
    --ink: #1c1c1c;
    --grid: #e4e4e4;
    --axis: #555555;
  }
  * { box-sizing: border-box; margin: 0; padding: 0; }
  html, body { width: 1200px; height: 1200px; overflow: hidden; }
  body {
    background: var(--backdrop);
    font-family: "Fira Sans", sans-serif;
    color: var(--ink);
    position: relative;
  }
  .slide {
    position: absolute;
    width: 563px;
    height: 317px;
    background: var(--slide);
    box-shadow: 0 2px 5px rgba(0,0,0,0.25);
    overflow: hidden;
  }
  .col-left { left: 22px; }
  .col-right { left: 616px; }
  .row-1 { top: 66px; }
  .row-2 { top: 440px; }
  .row-3 { top: 814px; }

  .brand-dot {
    position: absolute;
    top: 16px;
    right: 21px;
    width: 36px;
    height: 36px;
    border-radius: 50%;
    border: 3px solid var(--blue);
  }
  .frame {
    position: absolute;
    left: 26px;
    width: 502px;
    top: 70px;
    height: 220px;
    border: 4px solid var(--blue);
    background: var(--slide);
    box-shadow: 5px 5px 0 var(--green);
    display: flex;
    flex-direction: column;
    justify-content: center;
    align-items: center;
    text-align: center;
  }
  .accent { color: var(--blue); font-weight: 600; }

  /* Title slide */
  .cover-panel {
    position: absolute;
    left: 0; top: 0;
    width: 330px; height: 100%;
    background: var(--blue);
    border-right: 3px solid var(--green);
  }
  .cover-title {
    position: absolute;
    left: 32px; top: 196px;
    color: #fff;
    font-size: 30px;
    font-weight: 600;
  }
  .cover-date {
    position: absolute;
    left: 32px; top: 238px;
    color: #fff;
    font-size: 17px;
  }
  .cover-mark {
    position: absolute;
    left: 409px; top: 73px;
    width: 96px; height: 96px;
    border-radius: 50%;
    border: 4px solid var(--blue);
  }
  .cover-name {
    position: absolute;
    left: 330px; width: 233px;
    top: 196px;
    text-align: center;
    color: var(--blue);
    font-size: 34px;
    font-weight: 700;
    letter-spacing: 0.5px;
  }

  .slide-title {
    position: absolute;
    left: 32px;
    top: 30px;
    color: var(--blue);
    font-size: 27px;
    font-weight: 600;
  }
  .frame--tall { top: 70px; height: 218px; }
  .frame .lead { color: var(--blue); font-size: 17px; font-weight: 600; margin-bottom: 18px; }
  .frame .body { font-size: 19px; line-height: 25px; }

  .statement { font-size: 20px; line-height: 38px; padding: 0 24px; }
  .question { font-size: 22px; line-height: 45px; padding: 0 24px; }

  .heading-small {
    position: absolute;
    left: 32px; top: 26px;
    width: 440px;
    color: var(--blue);
    font-size: 15.5px;
    line-height: 20px;
    font-weight: 600;
  }
  .factor-list {
    list-style: none;
    align-self: flex-start;
    text-align: left;
    padding-left: 16px;
  }
  .factor-list li {
    position: relative;
    font-size: 11px;
    line-height: 21.2px;
    padding-left: 26px;
  }
  .factor-list li::before {
    content: "";
    position: absolute;
    left: 0; top: 9px;
    width: 4px; height: 4px;
    background: var(--blue);
  }
  .chart { position: absolute; left: 0; top: 0; }
  .chart text { font-family: "Fira Sans", sans-serif; fill: var(--axis); }
</style>
</head>
<body>

  <section class="slide col-left row-1">
    <div class="cover-panel"></div>
    <h1 class="cover-title">Presentation</h1>
    <p class="cover-date">Date</p>
    <div class="cover-mark"></div>
    <p class="cover-name">Norvale</p>
  </section>

  <section class="slide col-right row-1">
    <h2 class="slide-title">L’inaction…</h2>
    <div class="brand-dot"></div>
    <div class="frame frame--tall">
      <p class="lead">Vous croyez ne pas avoir les moyens d’épargner?</p>
      <p class="body">Pour générer 4$ par jour,<br>il ne suffit que de se faire son café et son muffin à<br>la maison le matin au lieu de l’acheter sur la route!<br>On ne parle pas ici d’un grand sacrifice pour<br>pouvoir espéré réaliser nos rêves!</p>
    </div>
  </section>

  <section class="slide col-left row-2">
    <div class="brand-dot"></div>
    <div class="frame">
      <p class="statement">Malheureusement, peu de gens arrivent à obtenir <span class="accent">l’indépendance financière</span> qui leur procurerait un tel niveau de sécurité et de liberté, pourtant ce rêve a été à la portée de presque tous…</p>
    </div>
  </section>

  <section class="slide col-right row-2">
    <div class="brand-dot"></div>
    <div class="frame">
      <p class="question"><span class="accent">L’idéal</span> pour beaucoup d’entre nous n’est-il pas d’avoir suffisamment <span class="accent">d’argent</span> et d’être en santé afin de pouvoir réaliser nos <span class="accent">rêves</span>?</p>
    </div>
  </section>

  <section class="slide col-left row-3">
    <h2 class="heading-small">Les principaux facteurs qui nuisent à l’atteinte de l’indépendance financière:</h2>
    <div class="brand-dot"></div>
    <div class="frame">
      <ul class="factor-list">
        <li>L’inaction et le report à plus tard</li>
        <li>Les erreurs émotives (la peur)</li>
        <li>Favoriser les plaisirs à court terme plutôt que les bénéfices à long terme</li>
        <li>Le manque de connaissances</li>
        <li>L’accès à l’information</li>
        <li>Les frais de gestion et la rémunération des conseiller financiers</li>
        <li>Les impôts</li>
        <li>L’inflation</li>
      </ul>
    </div>
  </section>

  <section class="slide col-right row-3">
    <h2 class="heading-small">Investissement fixe équivalent à 4$ par jour dans l’indice US 500 pour un individu né en 1950 et qui a commencé à épargner à 15 ans</h2>
    <div class="brand-dot"></div>
    <svg class="chart" width="563" height="317" viewBox="0 0 563 317" role="img" aria-label="Courbe de la valeur du placement de 1965 à 2015, atteignant environ 1,1 million de dollars">
      <g stroke="var(--grid)" stroke-width="1">
        <line x1="60" x2="540" y1="267" y2="267"/>
        <line x1="60" x2="540" y1="241.2" y2="241.2"/>
        <line x1="60" x2="540" y1="215.3" y2="215.3"/>
        <line x1="60" x2="540" y1="189.5" y2="189.5"/>
        <line x1="60" x2="540" y1="163.7" y2="163.7"/>
        <line x1="60" x2="540" y1="137.8" y2="137.8"/>
        <line x1="60" x2="540" y1="112" y2="112"/>
      </g>
      <line x1="60" x2="540" y1="267" y2="267" stroke="#bbb"/>
      <text x="32" y="107" font-size="9.5">$ million</text>
      <g font-size="9.5" text-anchor="end">
        <text x="49" y="270">0,0</text>
        <text x="49" y="244">0,2</text>
        <text x="49" y="218">0,4</text>
        <text x="49" y="193">0,6</text>
        <text x="49" y="167">0,8</text>
        <text x="49" y="141">1,0</text>
        <text x="49" y="115">1,2</text>
      </g>
      <g font-size="8.5" text-anchor="end">
        <text transform="translate(63 275) rotate(-90)">1965</text>
        <text transform="translate(82 275) rotate(-90)">1967</text>
        <text transform="translate(101 275) rotate(-90)">1969</text>
        <text transform="translate(121 275) rotate(-90)">1971</text>
        <text transform="translate(140 275) rotate(-90)">1973</text>
        <text transform="translate(159 275) rotate(-90)">1975</text>
        <text transform="translate(178 275) rotate(-90)">1977</text>
        <text transform="translate(197 275) rotate(-90)">1979</text>
        <text transform="translate(217 275) rotate(-90)">1981</text>
        <text transform="translate(236 275) rotate(-90)">1983</text>
        <text transform="translate(255 275) rotate(-90)">1985</text>
        <text transform="translate(274 275) rotate(-90)">1987</text>
        <text transform="translate(293 275) rotate(-90)">1989</text>
        <text transform="translate(313 275) rotate(-90)">1991</text>
        <text transform="translate(332 275) rotate(-90)">1993</text>
        <text transform="translate(351 275) rotate(-90)">1995</text>
        <text transform="translate(370 275) rotate(-90)">1997</text>
        <text transform="translate(389 275) rotate(-90)">1999</text>
        <text transform="translate(409 275) rotate(-90)">2001</text>
        <text transform="translate(428 275) rotate(-90)">2003</text>
        <text transform="translate(447 275) rotate(-90)">2005</text>
        <text transform="translate(466 275) rotate(-90)">2007</text>
        <text transform="translate(485 275) rotate(-90)">2009</text>
        <text transform="translate(505 275) rotate(-90)">2011</text>
        <text transform="translate(524 275) rotate(-90)">2013</text>
        <text transform="translate(543 275) rotate(-90)">2015</text>
      </g>
      <polyline fill="none" stroke="var(--blue)" stroke-width="2.2" stroke-linejoin="round"
        points="60,267 108,266 156,264 185,263 204,261 233,258 252,254 271,251 281,246 290,248 300,241 319,237 329,237 338,228 348,222 358,209 367,193 377,177 386,166 396,177 406,189 415,208 425,193 434,186 444,183 454,170 463,166 473,208 482,192 492,182 502,182 511,169 521,138 530,122 540,124"/>
    </svg>
  </section>

</body>
</html>
```